Redesign of page from emergency manual

Please redesign this PDF to look better. Please don't include any stock photos. It must be legible. Making some words bold is probably a good idea.

Here are some things I like :

https://tarrowbooks.com.au/collections/frontpage/products/the-plk-v2-ebook

https://img-cd.vostramediafiles.com/qa-ejkwPLOTYY_SuCKbZNu411Qwgjv8YssPxEdzXN93hDkSRjLXK8WmfgbmrJW4ZZ3yUPK=w1052-h592-rw

```html
<!DOCTYPE html>
<html lang="en">
<head>
<meta charset="utf-8">
<title>Hypertension, Acute</title>
<link rel="stylesheet" href="https://fonts.googleapis.com/css2?family=Montserrat:wght@300;400;500;700&display=swap">
<style>
  :root {
    --backdrop: #dcedf3;
    --page: #ffffff;
    --band: #8dd4ea;
    --ink: #1b1b1b;
    --rule: #1b1b1b;
  }
  * { box-sizing: border-box; margin: 0; padding: 0; }
  html, body { width: 1200px; height: 1200px; overflow: hidden; }
  body {
    background: var(--backdrop);
    font-family: "Montserrat", Arial, sans-serif;
    color: var(--ink);
    position: relative;
  }
  .page {
    position: absolute; left: 50px; top: 212px;
    width: 1100px; height: 775px;
    background: var(--page);
  }
  .page-header {
    position: absolute; left: 0; top: 0; width: 100%; height: 69px;
    background: var(--band);
  }
  .page-title {
    position: absolute; left: 40px; top: 21px;
    font-size: 22px; font-weight: 700;
  }
  .page-summary {
    position: absolute; left: 740px; top: 14px; width: 260px;
    text-align: center; font-size: 15px; font-weight: 400; line-height: 19px;
  }
  .intro {
    position: absolute; left: 40px; top: 86px; width: 570px;
    font-size: 15px; font-weight: 300; line-height: 19.5px;
  }
  .intro p { margin-bottom: 18px; }
  .intro p.tight { margin-bottom: 0; }
  .bp-table {
    position: absolute; left: 656px; top: 89px; width: 375px;
    border-collapse: collapse; font-size: 15px; font-weight: 300;
  }
  .bp-table th, .bp-table td { border: 1.5px solid var(--rule); }
  .bp-table .bp-caption-cell {
    background: var(--band); font-weight: 700; height: 25px; font-size: 15.5px;
  }
  .bp-table td { text-align: center; }
  .bp-table td:first-child { text-align: left; padding-left: 16px; }
  .bp-table tr.row-head td { height: 29px; }
  .bp-table tr.row-data td { height: 32px; }
  .side-label {
    position: absolute; left: 1062px; top: 381px;
    transform: translate(-50%, -50%) rotate(90deg);
    white-space: nowrap; font-size: 27px; font-weight: 700;
  }
  .caution {
    position: absolute; left: 40px; top: 260px; width: 975px;
    font-size: 15px; font-weight: 300; line-height: 19.5px;
  }
  .drug-table {
    position: absolute; left: 40px; top: 342px; width: 991px; height: 266px;
    border: 1.5px solid var(--rule); border-radius: 16px; overflow: hidden;
  }
  .drug-row { display: flex; border-top: 1.5px solid var(--rule); }
  .drug-row:first-child { border-top: 0; }
  .drug-action {
    width: 312px; flex: none; border-right: 1.5px solid var(--rule);
    display: flex; align-items: center; padding-left: 28px;
    font-size: 15px; font-weight: 400;
  }
  .drug-doses {
    flex: 1; display: flex; flex-direction: column; justify-content: center;
    padding-left: 38px; font-size: 15px; font-weight: 300; line-height: 19px;
  }
  .drug-row.head { background: var(--band); height: 45px; }
  .drug-row.head .drug-action { justify-content: center; padding-left: 0; font-size: 21px; font-weight: 700; }
  .drug-row.head .drug-doses { align-items: center; padding-left: 0; font-size: 21px; font-weight: 700; }
  .h-55 { height: 55px; }
  .h-66 { height: 66px; }
  .h-45 { height: 45px; }
  .differential {
    position: absolute; left: 0; top: 631px; width: 100%; height: 129px;
    background: var(--band);
  }
  .differential-title {
    position: absolute; left: 40px; top: 20px; font-size: 15px; font-weight: 700;
  }
  .differential-col {
    position: absolute; top: 53px; list-style: none;
    font-size: 15px; font-weight: 300; line-height: 19px;
  }
  .col-a { left: 40px; width: 360px; }
  .col-b { left: 412px; width: 440px; }
  .col-c { left: 862px; width: 220px; }
</style>
</head>
<body>
  <article class="page">
    <header class="page-header">
      <h1 class="page-title">Hypertension, Acute</h1>
      <p class="page-summary">Sustained high blood pressure refractory to treating reversible causes</p>
    </header>

    <section class="intro">
      <p>In pediatrics, hypertension is almost always treated by addressing likely causes such as light anesthesia or measurement error:</p>
      <p>• Ensure correct BP cuff size: cuff bladder width - 40% of limb circum-ference</p>
      <p class="tight">• Ensure arterial line transducer is at level of heart<br>- Consider placing arterial line if not already present</p>
    </section>

    <table class="bp-table">
      <tr><th class="bp-caption-cell" colspan="3">Hypertensive Blood Pressure Range*</th></tr>
      <tr class="row-head"><td>Age (yr)</td><td>Systolic</td><td>Diastolic</td></tr>
      <tr class="row-data"><td>newborn</td><td>&gt;97</td><td>&gt;70</td></tr>
      <tr class="row-data"><td>1-3</td><td>&gt;105</td><td>&gt;61</td></tr>
      <tr class="row-data"><td>4-12</td><td>&gt;113</td><td>&gt;86</td></tr>
    </table>

    <div class="side-label">Hypertension, Acute</div>

    <p class="caution">* CAUTION: Anti-hypertensive drugs are almost never needed for routine pediatric cases. These medications are used almost exclusively for specialized cardiac, neurosurgical, or endocrine (pheochromocytoma) cases. Consult an expert before use. Rule-out increased ICP.</p>

    <div class="drug-table">
      <div class="drug-row head">
        <div class="drug-action">Action</div>
        <div class="drug-doses">Drug (IV Dosing)</div>
      </div>
      <div class="drug-row h-55">
        <div class="drug-action">Direct smooth muscle relaxation</div>
        <div class="drug-doses">
          <span>§ Sodium nitroprusside 0.5-10 MICROgrams/kg/min</span>
          <span>§ HydrALAZINE 0.1-0.2 mg/kg (adult dose 5-10 mg)</span>
        </div>
      </div>
      <div class="drug-row h-66">
        <div class="drug-action">β-Adrenergic blockade</div>
        <div class="drug-doses">
          <span>Esmolol 100-500 MICROgrams/kg over 5 min, then</span>
          <span>25-300 MICROgrams/kg/min</span>
          <span>§ Labetalol (also a effect) 0.2-1 mg/kg q 10 min; 0.4-3 mg/kg/hour (infusion)</span>
        </div>
      </div>
      <div class="drug-row h-55">
        <div class="drug-action">Calcium channel blockade</div>
        <div class="drug-doses">
          <span>§ niCARdapine 0.5-5 MICROgrams/kg/min</span>
          <span>§ Clevidipine 0.5-3.5 MICROgrams/kg/min</span>
        </div>
      </div>
      <div class="drug-row h-45">
        <div class="drug-action">D1-dopamine agonist</div>
        <div class="drug-doses">
          <span>§ Fenoldopam 0.2-0.8 MICROgrams/kg/min</span>
        </div>
      </div>
    </div>

    <footer class="differential">
      <h2 class="differential-title">Consider Differential (Partial):</h2>
      <ul class="differential-col col-a">
        <li>• Light anesthesia (consider vaporizer or infusion pump empty or malfunctioning)</li>
        <li>• Hypercarbia</li>
      </ul>
      <ul class="differential-col col-b">
        <li>Hypoxemia</li>
        <li>• Arterial line transducer too low or BP cuff too small</li>
        <li>• Withdrawal (EtOH or opioid)</li>
      </ul>
      <ul class="differential-col col-c">
        <li>• Thyroid Storm</li>
        <li>• Pheochromocytoma</li>
        <li>• Drug Error</li>
      </ul>
    </footer>
  </article>
</body>
</html>
```